New Body Mist 250 ml exclusive

We are excited to embark on a new project to design the packaging for body mist:
Amber Drizzle

We are looking for a design that is truly unique and stands out, with a touch of individuality that sets it apart. The design should be eye-catching and visually appealing, drawing attention even from a distance. We want the body mists to have a fun and attractive look that appeals to customers.

To help bring your design to life, we will provide the dimensions of the bottle, which has a capacity of 250ml. The bottle measures 13.3 cm in height and 4.9 cm in diameter (excluding the pump). Additionally, we will also provide the dimensions of the label, which measures 15.1 cm in height and 12.8 cm in width.

We believe that giving you the freedom to put your own unique touch and color choices will help create a truly standout design. We look forward to seeing your creative vision for our body mist.

We shared with you the logo of the body mist and some examples of models that we liked.

Please be informed that the project only includes one design and the remaining three will be completed and paid for through a 1on1 project with the winner of the contest.

Target Market(s)

Supermarket and perfumery stores

Industry/Entity Type

Cosmetics

Font styles to use
Serif

Requirements
Must have
• Uniqueness and attractiveness

```html
<!DOCTYPE html>
<html lang="en">
<head>
<meta charset="utf-8">
<title>Amber Drizzle – Velvet Dusk Body Mist Label</title>
<link rel="stylesheet" href="https://fonts.googleapis.com/css2?family=Josefin+Sans:wght@400&family=Sacramento&family=Lato:wght@400&display=swap">
<style>
  :root {
    --backdrop: #a4509a;
    --label-blue: #33aacf;
    --bloom-magenta: rgba(162, 67, 154, 0.55);
    --ink-white: #ffffff;
  }
  * { margin: 0; padding: 0; box-sizing: border-box; }
  html, body {
    width: 1200px;
    height: 1200px;
    overflow: hidden;
    background: var(--backdrop);
  }
  .canvas {
    position: relative;
    width: 1200px;
    height: 1200px;
    display: flex;
    align-items: center;
    justify-content: center;
  }
  .label {
    position: relative;
    width: 800px;
    height: 904px;
    background: var(--label-blue);
    overflow: hidden;
  }
  .label__floral {
    position: absolute;
    inset: 0;
    background:
      radial-gradient(ellipse 260px 300px at 40px 200px, var(--bloom-magenta), transparent 70%),
      radial-gradient(ellipse 260px 320px at 780px 330px, var(--bloom-magenta), transparent 70%),
      radial-gradient(ellipse 300px 260px at 560px 740px, var(--bloom-magenta), transparent 70%),
      radial-gradient(ellipse 160px 120px at 150px 80px, var(--bloom-magenta), transparent 70%),
      var(--label-blue);
  }
  .label__brand {
    position: absolute;
    top: 46px;
    left: 0;
    right: 0;
    text-align: center;
    font-family: "Josefin Sans", sans-serif;
    font-weight: 400;
    font-variant: small-caps;
    font-size: 40px;
    letter-spacing: 5px;
    color: var(--ink-white);
  }
  .label__product {
    position: absolute;
    top: 390px;
    left: 40px;
    right: 40px;
    text-align: center;
    font-family: "Sacramento", cursive;
    font-weight: 400;
    font-size: 150px;
    line-height: 1;
    color: var(--ink-white);
    white-space: nowrap;
  }
  .label__volume {
    position: absolute;
    bottom: 24px;
    left: 0;
    right: 0;
    text-align: center;
    font-family: "Lato", sans-serif;
    font-size: 32px;
    color: var(--ink-white);
  }
</style>
</head>
<body>
  <main class="canvas">
    <section class="label">
      <div class="label__floral" role="img" aria-label="Line-drawn magenta lotus flowers with stems and white leaf strokes scattered over turquoise"></div>
      <p class="label__brand">Amber Drizzle</p>
      <h1 class="label__product">Velvet Dusk</h1>
      <p class="label__volume">250 ml</p>
    </section>
  </main>
</body>
</html>
```